New business card for a regional office of a US M&A company

We need business card for a finance company, office based in Hong Kong , our Head office is in US, our business is to Merge and acquires companies , the new office will be a regional office for the Asia Pacific region. We want to use the head office logo as attached ( but don't have to be exactly the same, can be a variation to it) as a base and then add Asia Pacific alongside the logo.
We would prefer to have be bilingual Eng + Chinese, although we don't really have Chinese company name .

Industry/Entity Type

Business

Contact Information for Business Card

Carla Beth Soren
 

VP,
APAC M&A Operations
Tovar Crest Asia Pacific Limited
 
Unit 1407, K82
27 Sai Lok Fung Road, 
Hong Kong 
 
M: +852 6481 2037
T : +852 2736 4100
F : +852 2736 4155
VOIP: 4813
 
cbsoren@tovarcrest.com

Font styles to use
Serif
Sans Serif

Colors

Designer to choose colors to be used in the design.

Requirements
Must have
• APAC Office

```html
<!DOCTYPE html>
<html lang="en">
<head>
<meta charset="utf-8">
<title>Tovar Crest – APAC Business Card</title>
<link href="https://fonts.googleapis.com/css2?family=Open+Sans:wght@700&family=Roboto:wght@300;400&family=Roboto+Condensed:wght@500&display=swap" rel="stylesheet">
<style>
  :root {
    --backdrop: #2a2a2a;
    --card-navy: #10283f;
    --accent-cyan: #1ba6d2;
    --text-light: #e6ebf0;
    --rule-grey: #8d9aa8;
    --band-white: #f2f2f2;
    --faint-block: #22405a;
  }
  * { margin: 0; padding: 0; box-sizing: border-box; }
  html, body { width: 1200px; height: 960px; overflow: hidden; background: var(--backdrop); }
  .canvas { position: relative; width: 1200px; height: 960px; }

  .card { position: absolute; background: var(--card-navy); overflow: hidden; }
  .card-front { left: 322px; top: 110px; width: 598px; height: 340px; }
  .card-back  { left: 320px; top: 493px; width: 600px; height: 343px; }

  .faint-block {
    position: absolute; left: 60px; top: 60px; width: 220px; height: 220px;
    background: var(--faint-block); opacity: .7;
  }
  .wordmark {
    position: absolute; right: 31px;
    font-family: "Open Sans", Arial, sans-serif; font-weight: 700;
    color: var(--accent-cyan); letter-spacing: .5px; white-space: nowrap; line-height: 1;
  }
  .card-front .wordmark { top: 248px; font-size: 44px; }
  .website {
    position: absolute; right: 31px; top: 294px;
    font-family: "Roboto", Arial, sans-serif; font-weight: 400; font-size: 14px;
    letter-spacing: 4.6px; color: var(--text-light); margin-right: -4.6px;
  }

  .brand-square {
    position: absolute; left: 438px; top: 60px; width: 40px; height: 40px;
    background: var(--band-white);
  }
  .card-back .wordmark { top: 118px; font-size: 38px; }

  .person-name {
    position: absolute; left: 31px; top: 166px;
    font-family: "Roboto Condensed", Arial Narrow, sans-serif; font-weight: 500;
    font-size: 22px; color: var(--accent-cyan); line-height: 1;
  }
  .person-title {
    position: absolute; left: 33px; top: 192px;
    font-family: "Roboto", Arial, sans-serif; font-size: 14px; color: var(--text-light); line-height: 1;
  }
  .title-rule {
    position: absolute; left: 60px; top: 199px; width: 509px; height: 1px; background: var(--rule-grey);
  }
  .contact-list {
    position: absolute; left: 32px; top: 219px; list-style: none;
    font-family: "Roboto", Arial, sans-serif; font-size: 14.5px; color: var(--text-light);
  }
  .contact-list li { display: flex; align-items: center; height: 19.5px; }
  .contact-list svg { width: 15px; height: 15px; margin-right: 8px; fill: var(--accent-cyan); }
  .voip {
    position: absolute; left: 32px; top: 285px;
    font-family: "Roboto", Arial, sans-serif; font-size: 14.5px; color: var(--text-light);
  }
  .office-address {
    position: absolute; right: 31px; top: 214px; text-align: right; font-style: normal;
    font-family: "Roboto", Arial, sans-serif; font-weight: 300; font-size: 14.5px;
    line-height: 18.6px; color: var(--text-light);
  }
  .office-address .unit { margin-top: 9px; }
  .footer-band { position: absolute; left: 0; bottom: 0; width: 600px; height: 13px; }
</style>
</head>
<body>
<main class="canvas">

  <section class="card card-front" aria-label="Card front">
    <div class="faint-block"></div>
    <div class="wordmark">TOVAR CREST</div>
    <div class="website">www.tovarcrest.com</div>
  </section>

  <section class="card card-back" aria-label="Card back">
    <div class="brand-square"></div>
    <div class="wordmark">TOVAR CREST</div>

    <h1 class="person-name">CARLA BETH SOREN</h1>
    <div class="person-title">VP</div>
    <div class="title-rule"></div>

    <ul class="contact-list">
      <li>
        <svg viewBox="0 0 16 16" aria-hidden="true"><path d="M3.2 1.2l2.4 2.8-1.3 1.8c.9 2 2.4 3.6 4.5 4.6l1.8-1.3 2.9 2.3-1.3 2.4C7.3 13.5 2.5 8.7 1.2 3.2z"/></svg>
        +852 2736 4100
      </li>
      <li>
        <svg viewBox="0 0 16 16" aria-hidden="true"><path d="M4.5 0h7a1 1 0 0 1 1 1v14a1 1 0 0 1-1 1h-7a1 1 0 0 1-1-1V1a1 1 0 0 1 1-1zm.6 2v10.5h5.8V2zM8 13.3a.9.9 0 1 0 0 1.8.9.9 0 0 0 0-1.8z"/></svg>
        +852 6481 2037
      </li>
      <li>
        <svg viewBox="0 0 16 16" aria-hidden="true"><path d="M4 1h6l2 2v3H4zM1 7h14v6h-2v-2H3v2H1zM4 12h8v3H4z"/></svg>
        +852 2736 4155
      </li>
    </ul>
    <div class="voip">VOIP: 4813</div>

    <address class="office-address">
      APAC M&amp;A Operations<br>
      Tovar Crest Asia Pacific Limited
      <div class="unit">Unit 1407, K82<br>27 Sai Lok Fung Road<br>Hong Kong</div>
    </address>

    <svg class="footer-band" viewBox="0 0 600 13" aria-hidden="true">
      <polygon points="0,0 393,0 389,13 0,13" fill="var(--accent-cyan)"/>
      <polygon points="397,0 600,0 600,13 393,13" fill="var(--band-white)"/>
    </svg>
  </section>

</main>
</body>
</html>
```